Business Card for Coach - ready to print

Design Business Card ready to order prints www.larsholm.coach

* An Overview / Background of the Business & Services
· Coaching
· Personal growth
* The Target Market / Audience you are trying to reach
· private person in different roles (self, familiy, business role)s
* Design Specifics; any preferences or ideas for Style, Colour, Imagery, etc
· See www.larsholm.coach
· "simple" design
· (small) element of surprise / unusual element

* Information that will be placed in the Business Card
· Beratung und Coaching
· Address: Lars Holm, Kesselgasse 7, CH-8517 Winterthur, Mobile +41 76 254 60 31
* Do you have an existing website or Facebook page where designers can learn more about your company?
· larsholm.coach

Target Market(s)

private person in different roles (self, familiy, business role)

Industry/Entity Type

Life Coaching

Contact Information for Business Card

Lars Holm
Kesselgasse 7
CH-8517 Winterthur

Mobile: +41 76 254 60 31
Email: laho@mailvale.ch
www.larsholm.coach

Font styles to use
Sans Serif

Colors

Designer to choose colors to be used in the design.

Requirements
Must have
• "simple" design
• element of surprise / unusual element
• Beratung & Coaching
• see www.larsholm.coach for colors and so...
Nice to have
• TA Symbol (three rings on top of each other) - unsual presentation
• QR Code of Website (see if it fits in and still looks good).

```html
<!DOCTYPE html>
<html lang="de">
<head>
<meta charset="utf-8">
<title>Lars Holm – Visitenkarte</title>
<link rel="stylesheet" href="https://fonts.googleapis.com/css2?family=Jost:wght@600&family=Questrial&display=swap">
<style>
  :root {
    --page-bg: #e4e4e4;
    --card-bg: #b8e0f7;
    --ink-strong: #1e1e1e;
    --ink-soft: #4d5157;
    --portrait-light: #a3a6aa;
    --portrait-dark: #6f7378;
    --card-shadow: rgba(0, 0, 0, 0.18);
  }
  * { margin: 0; padding: 0; box-sizing: border-box; }
  html, body {
    width: 1125px;
    height: 1200px;
    overflow: hidden;
    background: var(--page-bg);
  }
  .sheet {
    position: relative;
    width: 1125px;
    height: 1200px;
  }
  .card {
    position: absolute;
    left: 178px;
    width: 769px;
    height: 437px;
    background: var(--card-bg);
    box-shadow: 0 4px 14px var(--card-shadow);
  }
  .card--front { top: 140px; }
  .card--back  { top: 626px; }

  .portrait {
    position: absolute;
    left: 569px;
    top: 34px;
    width: 161px;
    height: 161px;
    border-radius: 50%;
    background: radial-gradient(circle at 50% 40%, var(--portrait-light), var(--portrait-dark));
  }

  .contact {
    position: absolute;
    left: 33px;
    top: 218px;
    font-family: "Questrial", "Century Gothic", sans-serif;
    color: var(--ink-soft);
  }
  .contact__name {
    font-family: "Jost", "Century Gothic", sans-serif;
    font-weight: 600;
    font-size: 24px;
    color: var(--ink-strong);
    line-height: 1;
    margin-bottom: 24px;
  }
  .contact__address {
    font-style: normal;
    font-size: 18px;
    line-height: 22px;
    margin-bottom: 14px;
  }
  .contact__list { list-style: none; }
  .contact__item {
    display: flex;
    align-items: center;
    font-size: 18px;
    height: 28.5px;
  }
  .contact__icon {
    width: 13px;
    height: 13px;
    margin-right: 8px;
    fill: var(--ink-strong);
    flex: none;
  }

  .tagline {
    position: absolute;
    inset: 0;
    display: flex;
    align-items: center;
    justify-content: center;
    padding-top: 2px;
    font-family: "Jost", "Century Gothic", sans-serif;
    font-weight: 600;
    font-size: 42px;
    color: var(--ink-strong);
  }
</style>
</head>
<body>
<main class="sheet">
  <section class="card card--front">
    <div class="portrait" role="img" aria-label="Porträtfoto von Lars Holm"></div>
    <div class="contact">
      <h1 class="contact__name">Lars Holm</h1>
      <address class="contact__address">Kesselgasse 7<br>CH-8517 Winterthur</address>
      <ul class="contact__list">
        <li class="contact__item">
          <svg class="contact__icon" viewBox="0 0 24 24" aria-hidden="true"><path d="M6.6 10.8c1.4 2.8 3.8 5.1 6.6 6.6l2.2-2.2c.3-.3.7-.4 1-.2 1.1.4 2.3.6 3.6.6.6 0 1 .4 1 1V20c0 .6-.4 1-1 1C10.6 21 3 13.4 3 4c0-.6.4-1 1-1h3.5c.6 0 1 .4 1 1 0 1.3.2 2.5.6 3.6.1.3 0 .7-.2 1L6.6 10.8z"/></svg>
          <span>+41 76 254 60 31</span>
        </li>
        <li class="contact__item">
          <svg class="contact__icon" viewBox="0 0 24 24" aria-hidden="true"><path d="M2 4h20v16H2V4zm3 3v10h2.5V10.5L12 15l4.5-4.5V17H19V7h-1.5L12 12.5 6.5 7H5z"/></svg>
          <span>laho@mailvale.ch</span>
        </li>
        <li class="contact__item">
          <svg class="contact__icon" viewBox="0 0 24 24" aria-hidden="true"><circle cx="12" cy="12" r="10"/><path d="M7 6.5c2 0 3 1.5 2.5 3S7 11 6 13s1 3 2.5 4M15 4.5c-.5 1.5.5 3 2 3s2.5 1.5 2 3-2 2-2.5 4" stroke="#b8e0f7" stroke-width="2" fill="none"/></svg>
          <span>www.larsholm.coach</span>
        </li>
      </ul>
    </div>
  </section>

  <section class="card card--back">
    <p class="tagline">Beratung &amp; Coaching</p>
  </section>
</main>
</body>
</html>
```